I need beautiful business cards with Moonpetals and sparrows on then and my tavolink business name is Moonpetals and sparrows.
I sell mini gardens, candles and melts and gift ware....on the other side I would like some thing like...REMEMBER to keep in touch with Moonpetals and sparrows buy a like,comment or just to say hello or tavo link will think you are no longer interested and delete you....you can change the wording to that to make smaller if you would like, and am not sure how to word it....my color theme for my business in purple and green. thank you.

tavo link:Moonpetals and sparrows
mini gardens
candles and melts
gift ware.
email:rosa514@kelvimail.com
phone:0873514062

```html
<!DOCTYPE html>
<html lang="en">
<head>
<meta charset="utf-8">
<title>Moonpetals and sparrows – business card</title>
<link rel="stylesheet" href="https://fonts.googleapis.com/css2?family=Arimo:wght@400;700&family=Kalam:wght@700&display=swap">
<style>
  :root {
    --page-bg: #ffffff;
    --violet-light: #9a80c4;
    --violet-mid: #7a5ca8;
    --violet-deep: #55357c;
    --violet-band: #4a2d6e;
    --leaf-green: #74c43c;
    --leaf-bright: #a4e04a;
    --card-text: #ffffff;
    --wisp: rgba(255, 255, 255, 0.22);
    --motif: rgba(160, 130, 200, 0.45);
  }
  * { box-sizing: border-box; margin: 0; padding: 0; }
  html, body {
    width: 1200px; height: 900px; overflow: hidden;
    background: var(--page-bg);
  }
  .stage {
    width: 1200px; height: 900px;
    display: flex; align-items: center; justify-content: center; gap: 44px;
  }
  .card {
    position: relative; width: 540px; height: 318px;
    border-radius: 26px; overflow: hidden;
    font-family: "Arimo", Arial, sans-serif; color: var(--card-text);
  }

  /* Front */
  .card--front {
    background: linear-gradient(160deg, var(--violet-light) 0%, var(--violet-mid) 55%, var(--violet-deep) 100%);
  }
  .front-wisps {
    position: absolute; right: 0; top: 0; width: 320px; height: 190px;
    background: radial-gradient(ellipse at 70% 40%, var(--wisp) 0%, rgba(255,255,255,0.06) 55%, transparent 75%);
  }
  .brand {
    position: absolute; left: 22px; top: 48px;
    font-family: "Arimo", Arial, sans-serif; font-weight: 700;
    font-size: 38px; line-height: 1.1; color: var(--leaf-green);
    text-transform: uppercase; letter-spacing: 0.5px;
  }
  .tagline {
    position: absolute; left: 22px; top: 138px;
    font-family: "Kalam", cursive; font-size: 19px; color: var(--card-text);
  }
  .contact-band {
    position: absolute; left: 0; right: 0; top: 182px; height: 90px;
    background: var(--violet-band);
    border-top: 4px solid var(--leaf-green);
    border-bottom: 4px solid var(--leaf-green);
    box-shadow: 0 -3px 0 var(--violet-deep), 0 3px 0 var(--violet-deep);
    display: flex; flex-direction: column; align-items: center; justify-content: center;
    font-size: 21px; line-height: 1.4;
  }
  .front-glow {
    position: absolute; left: 0; right: 0; bottom: 0; height: 42px;
    background: linear-gradient(90deg, var(--violet-mid), var(--violet-light) 40%, var(--violet-mid));
  }

  /* Back */
  .card--back { background: var(--violet-deep); }
  .motif-dragonflies {
    position: absolute; left: 28px; top: 14px; width: 130px; height: 120px;
    border-radius: 50%;
    background: radial-gradient(ellipse, var(--motif) 0%, transparent 70%);
  }
  .motif-butterflies {
    position: absolute; right: 14px; bottom: 24px; width: 150px; height: 170px;
    border-radius: 50%;
    background: radial-gradient(ellipse, var(--motif) 0%, transparent 70%);
  }
  .reminder {
    position: absolute; left: 20px; right: 20px; top: 86px;
    text-align: center; font-size: 17.5px; line-height: 1.35;
  }
  .reminder-name {
    display: block; color: var(--leaf-green); font-size: 18px;
    text-transform: uppercase; letter-spacing: 0.5px;
  }
</style>
</head>
<body>
  <main class="stage">
    <section class="card card--front" aria-label="Business card front">
      <div class="front-wisps" role="img" aria-label="Flowing light lines and sparkles"></div>
      <h1 class="brand">Moonpetals<br>and sparrows</h1>
      <p class="tagline">mini gardens candles and melts gift ware</p>
      <div class="contact-band">
        <span class="contact-phone">0873514062</span>
        <span class="contact-email">rosa514@kelvimail.com</span>
      </div>
      <div class="front-glow"></div>
    </section>

    <section class="card card--back" aria-label="Business card back">
      <div class="motif-dragonflies" role="img" aria-label="Faint dragonfly silhouettes"></div>
      <div class="motif-butterflies" role="img" aria-label="Faint butterfly silhouettes"></div>
      <p class="reminder">
        REMEMBER to keep in touch with
        <span class="reminder-name">Moonpetals and sparrows</span>
        buy a like,comment or just to say hello or<br>
        tavo link will think you are no longer interested<br>
        and delete you....
      </p>
    </section>
  </main>
</body>
</html>
```